Business Card Design Project for Web Development Company

Need a professional card that stands out with both color and texture.
We provide websites and web development services for small businesses with a focus on connections. Examples include: Automotive repair shop, we take their repair logs and make them available online so their customers can view, print and share (when selling) their maintenance records. Vet clinic, we create systems where customers can sign up for a recurring payment program for the annual wellness checks on their pets and get reminders when it's time, then see and schedule their own appointments. Etc... So not simply a website, but one that connects systems or customers to the business.
Important - !!!!We will be using http://inkvaleprinters.com/ for the cards, so take a look at what options are available for business card printing, they can do a lot of cool things!!!!
You can pick any 1-3 options from inkvaleprinters. I'm leaning towards a black background, but the logo will work on any color.
Front:
Marcus Telford
2750 SW 8th Ave STE 214-587
Carrow, WA 98512
541-617-2038 - cell
541-259-7306 - office
marcus@sitelinkhub.com
www.SiteLinkHub.com
Updates
We provide websites and web development services for small businesses with a focus on connections. Examples include: Automotive repair shop, we take their repair logs and make them available online so their customers can view, print and share (when selling) their maintenance records. Vet clinic, we create systems where customers can sign up for a recurring payment program for the annual wellness checks on their pets and get reminders when it''s time, then see and schedule their own appointments. Etc... So not simply a website, but one that connects systems or customers to the business.
Target Market(s)
Small business owners
Industry/Entity Type
Automotive
Look and feel
Each slider illustrates characteristics of the customer's brand and the style your logo design should communicate.

```html
<!DOCTYPE html>
<html lang="en">
<head>
<meta charset="utf-8">
<title>SiteLink Business Card</title>
<link rel="stylesheet" href="https://fonts.googleapis.com/css2?family=Carlito:wght@400;700&display=swap">
<style>
  :root {
    --page: #ffffff;
    --card-front: #262626;
    --card-back: #000000;
    --strip: #0b0b0b;
    --band: #2a2a2a;
    --accent: #2a9fdc;
    --muted: #6e6e6e;
    --muted-light: #858585;
  }
  * { margin: 0; padding: 0; box-sizing: border-box; }
  html, body {
    width: 996px; height: 1200px; overflow: hidden;
    background: var(--page);
    font-family: "Carlito", "Calibri", sans-serif;
  }
  .canvas { position: relative; width: 996px; height: 1200px; }

  .card { position: absolute; overflow: hidden; }
  .card--front { left: 4px; top: 4px; width: 984px; height: 562px; background: var(--card-front); }
  .card--back { left: 8px; top: 640px; width: 982px; height: 556px; background: var(--card-back); }

  .front-strip {
    position: absolute; right: 0; top: 0; width: 130px; height: 100%;
    background: var(--strip);
    display: flex; align-items: center; justify-content: center;
  }
  .brand {
    display: flex; align-items: center; gap: 12px;
    font-weight: 700; color: var(--accent); letter-spacing: 1px;
    line-height: 1;
  }
  .brand-dot { width: 0.42em; height: 0.42em; border-radius: 50%; background: var(--accent); }
  .brand--vertical {
    font-size: 80px;
    letter-spacing: 4px;
    transform: rotate(-90deg);
    white-space: nowrap;
  }

  .contact { position: absolute; left: 62px; top: 52px; }
  .contact-name { font-size: 49px; font-weight: 400; color: var(--accent); margin-bottom: 26px; }
  .contact-address { font-size: 28px; line-height: 36px; color: var(--muted); font-style: normal; }
  .contact-phones { margin-top: 52px; font-size: 28px; line-height: 38px; }
  .phone-label { display: inline-block; width: 120px; color: var(--muted); }
  .phone-number { color: var(--accent); }
  .contact-web { margin-top: 42px; font-size: 34px; line-height: 48px; color: var(--muted-light); }
  .contact-web .tld { color: var(--accent); }

  .back-band { position: absolute; left: 172px; top: 0; width: 160px; height: 100%; background: var(--band); }
  .brand--back { position: absolute; left: 176px; top: 456px; font-size: 68px; }
</style>
</head>
<body>
<main class="canvas">
  <section class="card card--front" aria-label="Card front">
    <div class="contact">
      <h1 class="contact-name">Marcus Telford</h1>
      <address class="contact-address">
        2750 SW 8th Ave STE 214-587<br>
        Carrow, WA 98512
      </address>
      <div class="contact-phones">
        <div><span class="phone-label">Cell&nbsp;&nbsp;&nbsp;&nbsp;&nbsp;:</span><span class="phone-number">360-617-2038</span></div>
        <div><span class="phone-label">Office :</span><span class="phone-number">360-259-7306</span></div>
      </div>
      <div class="contact-web">
        <div>marcus@sitelinkhub<span class="tld">.com</span></div>
        <div>www.SiteLinkHub<span class="tld">.com</span></div>
      </div>
    </div>
    <div class="front-strip">
      <div class="brand brand--vertical"><span>SiteLink</span><span class="brand-dot"></span></div>
    </div>
  </section>

  <section class="card card--back" aria-label="Card back">
    <div class="back-band"></div>
    <div class="brand brand--back"><span>SiteLink</span><span class="brand-dot"></span></div>
  </section>
</main>
</body>
</html>
```